Business Card for a recruitment agency specializing in engineers and geeks.

I am looking to create Business Card Design for my company.
That
## Company name:
Quorvant Inc.
Quorvant is a term coined from the following concepts.
1. geek + engineer
2. geek utopia
## Company Description:
The concept of the company is to be a recruitment agency that creates a paradise for geeky engineers. We want to be a place where engineers can have more freedom and ideal career support.
# Target.
The noun itself is often given to companies that want to hire engineers, geeks, and IT-related personnel, so it would be nice to get the impression that this company seems to have good engineers and IT personnel. There are many occasions where I meet with the human resources department, president, or senior management and give it to them.
# Atmosphere
We are happy with simplicity, but with an impact that will help people remember the company. The logo is based on a dinosaur that does programming, so it should be somewhat playful, but since it will basically be used in a business setting, please don't make it too silly.
# About the logo
See the attached files. The company logo represents our engineers smiling upward because of our work, with the motif of a dinosaur doing programming.
## Color
We will leave the color scheme to you, but since the logo is in black and white, colors with such a taste would fit well.
## file format
ai, psd, png, svg
Industry/Entity Type
human resource and employment agency
Contact Information for Business Card
Company name, address, email, tel, URL,logo
Colors
Designer to choose colors to be used in the design.

```html
<!DOCTYPE html>
<html lang="en">
<head>
<meta charset="utf-8">
<title>Quorvant Inc. Business Card</title>
<link href="https://fonts.googleapis.com/css2?family=Poppins:wght@400;500;600&display=swap" rel="stylesheet">
<style>
  :root {
    --backdrop: #232323;
    --card-white: #ffffff;
    --brand-blue: #1ca3ec;
    --brand-blue-deep: #1590d6;
    --ink: #1b1b1b;
    --rule: #9a9a9a;
  }
  * { margin: 0; padding: 0; box-sizing: border-box; }
  html, body {
    width: 1200px; height: 1108px; overflow: hidden;
    background: var(--backdrop);
    font-family: "Poppins", sans-serif;
  }
  .stage {
    width: 1200px; height: 1108px;
    display: flex; justify-content: center; align-items: center; gap: 60px;
  }
  .card {
    width: 400px; height: 660px; border-radius: 22px;
    position: relative; overflow: hidden;
  }
  .card--front {
    background: var(--card-white);
    display: flex; flex-direction: column; align-items: center;
    padding-top: 150px; text-align: center;
  }
  .brand-mark {
    display: flex; align-items: center; gap: 14px;
    color: var(--brand-blue); font-weight: 500; font-size: 62px; line-height: 1;
    letter-spacing: 0.5px;
  }
  .brand-mark__square {
    width: 26px; height: 26px; background: var(--brand-blue); border-radius: 4px;
  }
  .person-name {
    margin-top: 56px; color: var(--brand-blue); font-weight: 600; font-size: 32px; line-height: 1.1;
  }
  .person-title {
    color: var(--ink); font-size: 19px; line-height: 1.3;
  }
  .icon-divider {
    margin-top: 22px; width: 300px; display: flex; align-items: center; gap: 8px;
  }
  .icon-divider__line { flex: 1; height: 1px; background: var(--rule); }
  .contact-icon {
    width: 28px; height: 28px; background: var(--brand-blue); border-radius: 4px;
    display: flex; align-items: center; justify-content: center;
  }
  .contact-list {
    margin-top: 14px; color: var(--ink); font-size: 19px; line-height: 1.45;
  }
  .section-rule {
    margin-top: 16px; width: 300px; height: 1px; background: var(--rule);
  }
  .address {
    margin-top: 14px; color: var(--ink); font-size: 19px; line-height: 1.35;
  }
  .card--back {
    background: linear-gradient(150deg, #27adf0 0%, var(--brand-blue) 50%, var(--brand-blue-deep) 100%);
    display: flex; align-items: center; justify-content: center;
  }
  .back-pattern { position: absolute; inset: 0; }
  .back-brand {
    position: relative; color: #ffffff; font-weight: 500; font-size: 30px; margin-top: 240px;
  }
</style>
</head>
<body>
<main class="stage">
  <section class="card card--front">
    <div class="brand-mark"><span class="brand-mark__square"></span>Quorvant</div>
    <h1 class="person-name">Daniel Hartley</h1>
    <p class="person-title">Managing Director</p>
    <div class="icon-divider">
      <span class="icon-divider__line"></span>
      <span class="contact-icon">
        <svg width="18" height="18" viewBox="0 0 24 24"><path fill="#fff" d="M6.6 10.8a15 15 0 0 0 6.6 6.6l2.2-2.2c.3-.3.7-.4 1-.2 1.1.4 2.3.6 3.6.6.6 0 1 .4 1 1V20c0 .6-.4 1-1 1A17 17 0 0 1 3 4c0-.6.4-1 1-1h3.5c.6 0 1 .4 1 1 0 1.3.2 2.5.6 3.6.1.3 0 .7-.2 1z"/></svg>
      </span>
      <span class="contact-icon">
        <svg width="18" height="18" viewBox="0 0 24 24"><rect x="3" y="6" width="18" height="12" fill="none" stroke="#fff" stroke-width="2"/><path d="M3 6l9 7 9-7" fill="none" stroke="#fff" stroke-width="2"/></svg>
      </span>
      <span class="contact-icon">
        <svg width="18" height="18" viewBox="0 0 24 24"><circle cx="12" cy="12" r="9" fill="none" stroke="#fff" stroke-width="2"/><path d="M3 12h18M12 3c3 3 3 15 0 18M12 3c-3 3-3 15 0 18" fill="none" stroke="#fff" stroke-width="1.5"/></svg>
      </span>
      <span class="icon-divider__line"></span>
    </div>
    <p class="contact-list">
      044-555 201 730<br>
      hello@quorvantmail.com<br>
      www.quorvantsite.com
    </p>
    <div class="section-rule"></div>
    <p class="address">
      421, Address line goes here<br>
      45452,Country Name
    </p>
  </section>

  <section class="card card--back">
    <div class="back-pattern" role="img" aria-label="Repeating embossed brand pattern across the blue card back"></div>
    <div class="back-brand">Quorvant</div>
  </section>
</main>
</body>
</html>
```